Coach/consultant in conflict and challenge needs an enticing flyer

I need a double sided DL flyer design that will describe my work in helping people meet conflict and emotional challenge so they can learn and grow from these difficulties. I want to give a flavour of my style through fresh colours, repeated images used differently (the spiral), and a sense of positivity around conflict and difficulty. I want to attract people who are keen to do things differently and want to engage with creative processes rather than getting stuck in familiar patterns. My work is creative and often includes use of story, images and fables, so I want to convey that as well. I also place the work in a spiritual context, but grounded in practicality so I don't want it to seem New Age or flakey. I want something that seems innovative, professional and intriguing. I've included a sample of something I mocked up in word and also a copy of a flyer for Marla Quennet's Ember Gathering that inspired me to get a DL flyer. I want the design to communicate trust and transformation and engaging with fresh ways of doing things by moving past old habits

Target Market(s)

Mid 30s plus women and men who want to change their approach to conflict and emotional difficulties and are willing to take the creative and challenging journey to do that

Industry/Entity Type

Learn

Colors
acd136
00a990

Requirements
Must have
• a shift in the use of the spiral image,
• use of image of me (Norah)
• bright fresh colours olours that represent growth and transformation--I've suggested lime green as it suggests a sense of growth
• easy to read text
Nice to have
• Interesting non-traditional fonts perhaps text in a contemporary sans serif and another brush script font (like the Ember Gathering example)
• bleed to the edge and run off the page images or text
Should not have
• anything that represents too much tradition or stuckness

```html
<!DOCTYPE html>
<html lang="en">
<head>
<meta charset="utf-8">
<title>Norah Wrenfield — DL Flyer</title>
<link rel="stylesheet" href="https://fonts.googleapis.com/css2?family=Caveat+Brush&family=Kaushan+Script&family=Mulish:ital,wght@0,300;0,400;1,300;1,400&display=swap">
<style>
  :root {
    --page-bg: #efece6;
    --lime: #9cc531;
    --lime-deep: #8cb726;
    --lime-ring: #6d8f2a;
    --lime-faint: rgba(60, 90, 20, 0.13);
    --teal: #1db49c;
    --ink: #3b2a22;
    --ink-soft: #2e2a26;
    --white: #ffffff;
    --paper: #f1f1ef;
    --brush-brown: #6b3d1d;
    --accent-orange: #e4572e;
  }
  * { box-sizing: border-box; margin: 0; padding: 0; }
  html, body { width: 1143px; height: 1200px; overflow: hidden; }
  body { background: var(--page-bg); position: relative; font-family: "Mulish", sans-serif; color: var(--ink-soft); }

  .flyer { position: absolute; left: 30px; width: 1083px; height: 527px; overflow: hidden; box-shadow: 0 4px 14px rgba(0,0,0,0.25); }
  .flyer--front { top: 60px; background: var(--lime); }
  .flyer--back { top: 626px; background: var(--teal); }

  /* Front */
  .front-side-panel { position: absolute; left: 0; top: 0; width: 367px; height: 100%; background: var(--paper); }
  .bamboo-art { position: absolute; left: 140px; top: 0; width: 260px; height: 100%;
    background: linear-gradient(90deg, rgba(140,190,40,0) 0%, rgba(120,180,40,0.55) 40%, rgba(90,150,30,0.75) 62%, rgba(140,190,40,0) 100%); }
  .name-watermark { position: absolute; left: 70px; top: 385px; font-family: "Caveat Brush", cursive; font-size: 190px; line-height: 1; color: var(--lime-faint); white-space: nowrap; }
  .brand { position: absolute; left: 412px; top: 42px; display: flex; align-items: center; gap: 16px; }
  .brand-name { font-family: "Caveat Brush", cursive; font-weight: 400; font-size: 84px; line-height: 1; color: var(--ink); white-space: nowrap; }
  .brand-dot { width: 60px; height: 60px; border-radius: 50%; background: var(--lime-deep); border: 6px solid var(--lime-ring); }
  .tagline { position: absolute; left: 423px; top: 162px; font-family: "Kaushan Script", cursive; font-size: 30px; color: var(--white); word-spacing: 12px; white-space: nowrap; }
  .intro { position: absolute; left: 490px; top: 224px; width: 550px; font-size: 18px; line-height: 29px; color: var(--ink-soft); text-align: right; }
  .about { position: absolute; left: 407px; top: 346px; width: 630px; font-size: 18px; line-height: 29px; font-style: italic; color: var(--ink-soft); text-align: justify; }

  /* Back */
  .back-copy { position: absolute; left: 40px; width: 600px; font-size: 17px; line-height: 24px; color: var(--ink-soft); }
  .back-copy--first { top: 46px; }
  .back-copy--second { top: 187px; }
  .contact { position: absolute; left: 40px; top: 298px; list-style: none; }
  .contact-name { font-size: 18px; line-height: 22px; }
  .contact-creds { font-size: 13px; line-height: 20px; margin-bottom: 6px; }
  .contact-line { display: flex; align-items: center; gap: 6px; font-size: 16px; line-height: 24px; }
  .contact-icon { width: 14px; height: 14px; flex: none; }
  .contact-abn { font-size: 14px; margin-top: 12px; }
  .services { position: absolute; left: 370px; top: 326px; width: 270px; text-align: center; font-family: "Kaushan Script", cursive; font-size: 28px; line-height: 40px; color: var(--ink); }
  .portrait { position: absolute; left: 630px; top: 0; width: 453px; height: 527px; }
</style>
</head>
<body>

<section class="flyer flyer--front" aria-label="Flyer front">
  <div class="front-side-panel"></div>
  <div class="name-watermark" aria-hidden="true">Norah Wrenfield</div>
  <div class="bamboo-art" role="img" aria-label="Illustration of green bamboo stalks and leaves"></div>

  <div class="brand">
    <h1 class="brand-name">Norah Wrenfield</h1>
    <span class="brand-dot" aria-hidden="true"></span>
  </div>
  <p class="tagline">#courage #listening #creativity</p>
  <p class="intro">Challenge, change and conflict are a natural part of life. When we greet them with courage, and listen to what they tell us, we grow in wisdom, resilience and creativity.</p>
  <p class="about">Norah Wrenfield is a coach, educator and mediator. She works with people who want to harvest the fruits of challenge and conflict so they live life differently.</p>
</section>

<section class="flyer flyer--back" aria-label="Flyer back">
  <p class="back-copy back-copy--first">Consult with Norah to address challenges in your life, relationship, group or organisation. Through listening, conversation and creative processes, you will discover what your challenge is asking of you. Norah Wrenfield is a skilled facilitator who works to shift people’s responses from reactivity to creativity.</p>
  <p class="back-copy back-copy--second">With many years’ experience in coaching and mentorship, mediation and narrative processes, Norah supports you to uncover unique responses to difficult situations.</p>

  <ul class="contact">
    <li class="contact-name">Norah Wrenfield</li>
    <li class="contact-creds">PhD, MCR, BAppSci, DipHum, AssDipEd</li>
    <li class="contact-line"><svg class="contact-icon" viewBox="0 0 14 14"><circle cx="7" cy="7" r="6" fill="none" stroke="var(--accent-orange)" stroke-width="1.5"/></svg>0400 555 182 (m)</li>
    <li class="contact-line"><svg class="contact-icon" viewBox="0 0 14 14"><circle cx="7" cy="7" r="6" fill="none" stroke="var(--accent-orange)" stroke-width="1.5"/></svg>+61 3 9000 4417 (h)</li>
    <li class="contact-line"><svg class="contact-icon" viewBox="0 0 14 14"><circle cx="7" cy="7" r="6" fill="none" stroke="var(--accent-orange)" stroke-width="1.5"/></svg>norah@norahwrenfield.com</li>
    <li class="contact-line"><svg class="contact-icon" viewBox="0 0 14 14"><circle cx="7" cy="7" r="6" fill="none" stroke="var(--accent-orange)" stroke-width="1.5"/></svg>norahwrenfield.com</li>
    <li class="contact-abn">ABN 12 345 678 90</li>
  </ul>

  <p class="services">Consultations<br>Articles • Speaking<br>Workshops</p>

  <svg class="portrait" viewBox="0 0 453 527">
    <defs>
      <linearGradient id="photoBg" x1="0" y1="0" x2="0" y2="1">
        <stop offset="0" stop-color="#f3f2ef"/>
        <stop offset="1" stop-color="#e9e6e1"/>
      </linearGradient>
      <radialGradient id="photoFill" cx="0.5" cy="0.45" r="0.6">
        <stop offset="0" stop-color="#c9b8a8"/>
        <stop offset="0.55" stop-color="#d98a5a"/>
        <stop offset="1" stop-color="#e2572a"/>
      </radialGradient>
    </defs>
    <rect x="85" y="0" width="368" height="527" fill="url(#photoBg)"/>
    <circle cx="285" cy="290" r="200" fill="url(#photoFill)" role="img" aria-label="Portrait photograph of Norah in an orange knitted top"/>
    <circle cx="285" cy="290" r="222" fill="none" stroke="var(--brush-brown)" stroke-width="32"/>
  </svg>
</section>

</body>
</html>
```